Stonebay Towing Business Card

Towing
Accident towing
Mechanical breakdown
Insurance, salvage and recovery
4wd off road towing
Light & Heavy towing
8347 2516
24 hour business 7 days

Logo can be whole size on front

Industry/Entity Type

Towing/ transport

Contact Information for Business Card

The above

```html
<!DOCTYPE html>
<html lang="en">
<head>
<meta charset="utf-8">
<title>Stonebay Towing Business Card</title>
<link href="https://fonts.googleapis.com/css2?family=Roboto:wght@500;700&display=swap" rel="stylesheet">
<style>
  :root {
    --page: #d6d6d6;
    --card: #ffffff;
    --red: #d6212b;
    --black: #0b0b0b;
    --ink: #1a1a1a;
    --white: #ffffff;
  }
  * { box-sizing: border-box; margin: 0; padding: 0; }
  html, body { width: 1200px; height: 3000px; overflow: hidden; background: var(--page); }
  body { position: relative; font-family: "Roboto", sans-serif; }

  .card {
    position: absolute;
    left: 115px;
    width: 970px;
    height: 555px;
    background: var(--card);
    overflow: hidden;
  }
  .card--back { top: 897px; }
  .card--front { top: 1547px; }

  .card__wave { position: absolute; inset: 0; width: 970px; height: 555px; }
  .wave-red { fill: var(--red); }
  .wave-black { fill: var(--black); }

  .brand-name {
    position: absolute;
    left: 0; right: 0;
    text-align: center;
    color: var(--red);
    font-weight: 700;
    letter-spacing: 1px;
    white-space: nowrap;
  }
  .card--back .brand-name { top: 70px; font-size: 66px; }
  .card--front .brand-name { top: 120px; font-size: 104px; }

  .services { position: absolute; top: 0; left: 0; width: 100%; height: 100%; list-style: none; }
  .service {
    position: absolute;
    display: flex;
    align-items: flex-start;
    gap: 16px;
    color: var(--ink);
    font-weight: 500;
    font-size: 24px;
    line-height: 28px;
  }
  .service__tick { flex: 0 0 32px; width: 32px; height: 32px; margin-top: -4px; }
  .tick-box { fill: var(--red); }
  .tick-mark { fill: none; stroke: var(--white); stroke-width: 2.4; stroke-linecap: round; stroke-linejoin: round; }

  .contact { position: absolute; left: 48px; list-style: none; color: var(--white); font-weight: 700; }
  .contact__item { display: flex; align-items: center; gap: 12px; margin-bottom: 18px; }
  .contact__icon { width: 34px; height: 34px; }
  .icon-disc { fill: var(--red); }
  .icon-line { fill: none; stroke: var(--white); stroke-width: 2.2; stroke-linecap: round; }
  .icon-fill { fill: var(--white); }
  .card--back .contact { top: 448px; font-size: 23px; }
  .card--front .contact { top: 428px; font-size: 23px; left: 58px; }
</style>
</head>
<body>

<section class="card card--back" aria-label="Business card back">
  <svg class="card__wave" viewBox="0 0 970 555" aria-hidden="true">
    <path class="wave-red" d="M0 393 C250 318 450 470 640 512 C800 545 900 480 970 428 L970 555 L0 555 Z"/>
    <path class="wave-black" d="M0 433 C250 370 450 508 650 540 C820 565 910 505 970 456 L970 555 L0 555 Z"/>
  </svg>

  <div class="brand-name">Stonebay Towing</div>

  <ul class="services">
    <li class="service" style="left:59px;top:262px">
      <svg class="service__tick" viewBox="0 0 32 32" aria-hidden="true"><rect class="tick-box" width="32" height="32" rx="5"/><path class="tick-mark" d="M9 16.5l4.5 4.5 9.5-10"/></svg>
      <span>Towing</span>
    </li>
    <li class="service" style="left:59px;top:324px">
      <svg class="service__tick" viewBox="0 0 32 32" aria-hidden="true"><rect class="tick-box" width="32" height="32" rx="5"/><path class="tick-mark" d="M9 16.5l4.5 4.5 9.5-10"/></svg>
      <span>Mechanical breakdown</span>
    </li>
    <li class="service" style="left:361px;top:262px">
      <svg class="service__tick" viewBox="0 0 32 32" aria-hidden="true"><rect class="tick-box" width="32" height="32" rx="5"/><path class="tick-mark" d="M9 16.5l4.5 4.5 9.5-10"/></svg>
      <span>Accident towing</span>
    </li>
    <li class="service" style="left:361px;top:315px">
      <svg class="service__tick" viewBox="0 0 32 32" aria-hidden="true"><rect class="tick-box" width="32" height="32" rx="5"/><path class="tick-mark" d="M9 16.5l4.5 4.5 9.5-10"/></svg>
      <span>Insurance, salvage<br>and recovery</span>
    </li>
    <li class="service" style="left:634px;top:260px">
      <svg class="service__tick" viewBox="0 0 32 32" aria-hidden="true"><rect class="tick-box" width="32" height="32" rx="5"/><path class="tick-mark" d="M9 16.5l4.5 4.5 9.5-10"/></svg>
      <span>Light &amp; Heavy towing</span>
    </li>
    <li class="service" style="left:634px;top:322px">
      <svg class="service__tick" viewBox="0 0 32 32" aria-hidden="true"><rect class="tick-box" width="32" height="32" rx="5"/><path class="tick-mark" d="M9 16.5l4.5 4.5 9.5-10"/></svg>
      <span>4wd off road towing</span>
    </li>
  </ul>

  <ul class="contact">
    <li class="contact__item">
      <svg class="contact__icon" viewBox="0 0 34 34" aria-hidden="true"><circle class="icon-disc" cx="17" cy="17" r="17"/><path class="icon-fill" d="M11.5 9.5c1-.6 2-.4 2.6.5l1.6 2.6c.5.8.3 1.8-.4 2.3l-1 .8c.9 2 2.4 3.5 4.4 4.4l.8-1c.5-.7 1.5-.9 2.3-.4l2.6 1.6c.9.6 1.1 1.6.5 2.6l-.8 1.2c-.7 1-2 1.4-3.2 1-5.2-1.6-9.3-5.7-10.9-10.9-.4-1.2 0-2.5 1-3.2z"/></svg>
      <span>8347 2516</span>
    </li>
    <li class="contact__item">
      <svg class="contact__icon" viewBox="0 0 34 34" aria-hidden="true"><circle class="icon-disc" cx="17" cy="17" r="17"/><circle class="icon-line" cx="17" cy="17" r="9"/><path class="icon-line" d="M17 11.5V17l3.5 2.5"/></svg>
      <span>24 hour business 7 days</span>
    </li>
  </ul>
</section>

<section class="card card--front" aria-label="Business card front">
  <svg class="card__wave" viewBox="0 0 970 555" aria-hidden="true">
    <path class="wave-red" d="M0 365 C250 295 450 455 650 495 C810 525 905 470 970 410 L970 555 L0 555 Z"/>
    <path class="wave-black" d="M0 405 C250 345 450 492 660 522 C825 545 910 490 970 440 L970 555 L0 555 Z"/>
  </svg>

  <div class="brand-name">Stonebay Towing</div>

  <ul class="contact">
    <li class="contact__item">
      <svg class="contact__icon" viewBox="0 0 34 34" aria-hidden="true"><circle class="icon-disc" cx="17" cy="17" r="17"/><path class="icon-fill" d="M11.5 9.5c1-.6 2-.4 2.6.5l1.6 2.6c.5.8.3 1.8-.4 2.3l-1 .8c.9 2 2.4 3.5 4.4 4.4l.8-1c.5-.7 1.5-.9 2.300-.4l2.6 1.6c.9.6 1.1 1.6.5 2.6l-.8 1.2c-.7 1-2 1.4-3.2 1-5.2-1.6-9.3-5.7-10.9-10.9-.4-1.2 0-2.5 1-3.2z"/></svg>
      <span>8347 2516</span>
    </li>
    <li class="contact__item">
      <svg class="contact__icon" viewBox="0 0 34 34" aria-hidden="true"><circle class="icon-disc" cx="17" cy="17" r="17"/><circle class="icon-line" cx="17" cy="17" r="9"/><path class="icon-line" d="M17 11.5V17l3.5 2.5"/></svg>
      <span>24 hour business 7 days</span>
    </li>
  </ul>
</section>

</body>
</html>
```